Website design project for ICT Business - Bright Harbour Tx

We need website built for our new startup. The company name is Bright Harbour TX. Bright Harbour is an Information Communication Technology business that aims to help small to medium businesses unlock the power and benefits of the cloud. We are a sales and support business that consults with our clients to assist them in migrating to the cloud safely and without business interruption.

Coding

Coded - Design and coding required

Number of Pages Required

4 page

```html
<!DOCTYPE html>
<html lang="en">
<head>
<meta charset="utf-8">
<title>Bright Harbour</title>
<link href="https://fonts.googleapis.com/css2?family=Open+Sans:wght@300;400;600;700&display=swap" rel="stylesheet">
<style>
:root{
  --sky:#0aa6e6;
  --navy:#0b5a9e;
  --deep:#075c9c;
  --text:#8a8a8a;
  --dark:#555;
  --paper:#fafafa;
  --band:#f3f3f3;
  --white:#fff;
}
*{margin:0;padding:0;box-sizing:border-box}
html,body{width:1200px;height:2848px;overflow:hidden}
body{position:relative;background:var(--white);font-family:'Open Sans',Arial,sans-serif;color:var(--text)}
.abs{position:absolute}
.backdrop{position:absolute;left:0;top:0}
.brand{left:144px;top:44px;color:var(--white);text-align:center;line-height:1}
.brand-name{font-size:24px;font-weight:700;letter-spacing:-.5px}
.brand-sub{font-size:7px;letter-spacing:1.5px;margin-top:4px;text-transform:uppercase}
.nav{top:66px;left:385px;font-size:16px;color:var(--white)}
.nav a{color:inherit;text-decoration:none;position:absolute;white-space:nowrap}
.nav .active{border-bottom:3px solid var(--deep);padding-bottom:6px}
.hero-title{left:144px;top:242px;font-size:27px;font-weight:600;color:var(--white)}
.hero-sub{left:144px;top:286px;font-size:20px;font-weight:300;color:var(--white);line-height:27px;width:340px}
.btn{left:146px;top:365px;width:107px;height:33px;background:var(--deep);color:var(--white);font-size:12px;font-weight:600;display:flex;align-items:center;justify-content:center;letter-spacing:.3px}
.hero-art{left:608px;top:165px;width:418px;height:310px;border-radius:16px;background:linear-gradient(180deg,#ffffff,#dbeaf6)}
.slider-dots{left:1155px;top:392px;display:flex;flex-direction:column;gap:10px}
.slider-dots span{width:10px;height:10px;border-radius:50%;background:var(--white)}
.slider-dots .on{background:var(--deep)}
.section-title{left:0;width:1200px;text-align:center;font-size:25px;font-weight:600;color:var(--navy)}
.lead{left:150px;width:900px;text-align:center;font-size:15px;line-height:31px}
.feature{width:390px;text-align:center}
.feature-icon{width:124px;height:124px;border-radius:50%;background:var(--navy);margin:0 auto;display:flex;align-items:center;justify-content:center}
.feature h3{font-size:25px;font-weight:600;color:var(--navy);margin-top:24px}
.feature p{font-size:15px;line-height:31px;margin-top:16px}
.client{top:1614px;font-size:30px;font-weight:600;color:#555;white-space:nowrap;display:flex;align-items:center;gap:10px}
.client-mark{width:22px;height:22px;background:#7cc242}
.avatar{left:224px;top:2003px;width:290px;height:213px;border-radius:12px;background:linear-gradient(180deg,#f1f4f7,#c9d6e2)}
.quote-mark{left:550px;top:2010px;font-size:110px;line-height:1;font-weight:700;color:var(--sky);font-family:Georgia,serif}
.person{left:632px;top:2016px;font-size:27px;color:#555}
.company{left:633px;top:2052px;font-size:13px;color:#aaa}
.quote{left:562px;top:2092px;width:480px;font-size:15px;line-height:31px}
.pager{left:566px;top:2296px;display:flex;gap:10px}
.pager span{width:10px;height:10px;border-radius:50%;background:#d6d6d6}
.pager .on{background:var(--navy)}
.footer-brand{left:0;width:1200px;top:2420px;text-align:center;color:var(--navy);line-height:1}
.footer-brand .brand-name{font-size:34px}
.footer-brand .brand-sub{font-size:9px}
.links{top:2557px;list-style:none;font-size:13px;color:#555}
.links li{height:31px}
.contact{left:562px;top:2557px;list-style:none;font-size:13px;color:#555}
.contact li{display:flex;gap:14px;height:42px;align-items:flex-start}
.contact svg{flex:none;margin-top:2px}
.social{left:828px;top:2560px;display:flex;gap:18px}
.social span{width:27px;height:27px;border-radius:50%;border:1.5px solid #bbb}
.rule{left:0;top:2795px;width:1200px;height:1px;background:#e6e6e6}
.copyright{left:0;width:1200px;top:2817px;text-align:center;font-size:13px;color:#555}
</style>
</head>
<body>
<svg class="backdrop" width="1200" height="2848" viewBox="0 0 1200 2848" aria-hidden="true">
  <rect x="0" y="0" width="1200" height="2848" fill="var(--paper)"/>
  <polygon points="0,0 1200,0 1200,524 598,621 0,524" fill="var(--sky)"/>
  <polygon points="0,389 598,621 0,524" fill="var(--deep)"/>
  <polygon points="910,0 1200,0 1200,10 1040,50" fill="var(--deep)"/>
  <polygon points="1040,50 1200,10 1200,0 1120,0" fill="#1f9be0"/>
  <polygon points="0,915 600,1010 1200,915 1200,2848 0,2848" fill="var(--white)"/>
  <polygon points="0,1520 600,1445 1200,1520 1200,1745 600,1830 0,1745" fill="var(--band)"/>
  <polygon points="0,2465 600,2360 1200,2465 1200,2795 0,2795" fill="var(--paper)"/>
</svg>

<header>
  <div class="abs brand"><div class="brand-name">brightharbour</div><div class="brand-sub">Texas Coast</div></div>
  <nav class="abs nav">
    <a class="active" style="left:0">HOME</a>
    <a style="left:80px">ABOUT US</a>
    <a style="left:187px">SERVICES</a>
    <a style="left:285px">SOLUTIONS</a>
    <a style="left:403px">CLIENTS</a>
    <a style="left:494px">CONTACT US</a>
  </nav>
</header>

<section class="hero">
  <h1 class="abs hero-title">Bright Harbour</h1>
  <p class="abs hero-sub">Bright Harbour is an Information Communication Technology business</p>
  <div class="abs btn">LEARN MORE</div>
  <div class="abs hero-art" role="img" aria-label="Illustration of cloud services with business charts and data"></div>
  <div class="abs slider-dots"><span class="on"></span><span></span><span></span><span></span></div>
</section>

<section class="about">
  <h2 class="abs section-title" style="top:700px">ABOUT THE BUSINESS</h2>
  <p class="abs lead" style="top:764px">Sed ut perspiciatis unde omnis iste natus error sit voluptatem accusantium doloremque laudantium, totam rem aperiam, eaque ipsa quae ab illo inventore veritatis et quasi architecto beatae vitae dicta sunt explicabo. Nemo enim ipsam voluptatem quia voluptas sit aspernatur aut odit aut fugit, sed quia consequuntur magni dolores eos qui ratione</p>
</section>

<section class="features">
  <div class="abs feature" style="left:166px;top:1102px">
    <div class="feature-icon"><svg width="60" height="60" viewBox="0 0 60 60"><path d="M6 8 Q6 6 8 6 H28 L54 32 Q56 34 54 36 L36 54 Q34 56 32 54 L6 28 Z" fill="#fff"/><circle cx="18" cy="18" r="5" fill="var(--navy)"/></svg></div>
    <h3>SALES</h3>
    <p>Sed ut perspiciatis unde omnis iste natus error sit voluptatem accusantium doloremque laudantium, totam rem aperiam, eaque ipsa quae</p>
  </div>
  <div class="abs feature" style="left:635px;top:1102px">
    <div class="feature-icon"><svg width="66" height="66" viewBox="0 0 66 66"><circle cx="33" cy="33" r="27" fill="none" stroke="#fff" stroke-width="9"/><circle cx="33" cy="33" r="10" fill="none" stroke="#fff" stroke-width="6"/><g stroke="#fff" stroke-width="9"><line x1="33" y1="4" x2="33" y2="22"/><line x1="33" y1="44" x2="33" y2="62"/><line x1="4" y1="33" x2="22" y2="33"/><line x1="44" y1="33" x2="62" y2="33"/></g><g stroke="var(--navy)" stroke-width="3"><line x1="14" y1="14" x2="24" y2="24"/><line x1="42" y1="42" x2="52" y2="52"/><line x1="52" y1="14" x2="42" y2="24"/><line x1="14" y1="52" x2="24" y2="42"/></g></svg></div>
    <h3>SUPPORT</h3>
    <p>Sed ut perspiciatis unde omnis iste natus error sit voluptatem accusantium doloremque laudantium, totam rem aperiam, eaque ipsa quae</p>
  </div>
</section>

<section class="clients">
  <h2 class="abs section-title" style="top:1524px">CLIENTS</h2>
  <div class="abs client" style="left:184px">Norvale</div>
  <div class="abs client" style="left:376px">Tidewell</div>
  <div class="abs client" style="left:560px">Quarrystack</div>
  <div class="abs client" style="left:778px">Kestrel Partner<span class="client-mark"></span></div>
</section>

<section class="testimonials">
  <h2 class="abs section-title" style="top:1900px">WHAT CUSTOMERS SAY ABOUT US</h2>
  <div class="abs avatar" role="img" aria-label="Portrait photo of a customer"></div>
  <div class="abs quote-mark">“</div>
  <div class="abs person">Daniel Reyes</div>
  <div class="abs company">Company Name</div>
  <p class="abs quote">Sed ut perspiciatis unde omnis iste natus error sit voluptatem accusantium doloremque laudantium, totam rem aperiam, eaque ipsa quae ab illo inventore veritatis et quasi architecto beatae vitae dicta sunt explicabo.</p>
  <div class="abs pager"><span class="on"></span><span></span><span></span><span></span></div>
</section>

<footer>
  <div class="abs footer-brand"><div class="brand-name">brightharbour</div><div class="brand-sub">Texas Coast</div></div>
  <ul class="abs links" style="left:144px"><li>Home</li><li>About us</li><li>Services</li><li>Solutions</li><li>Clients</li><li>Contact Us</li></ul>
  <ul class="abs links" style="left:380px"><li>Terms &nbsp;Of Use</li><li>Privacy Policy</li><li>Help</li><li>Disclaimer</li></ul>
  <ul class="abs contact">
    <li><svg width="14" height="14" viewBox="0 0 14 14"><path d="M3 1 L5 4 L4 5.5 Q5.5 8.5 8.5 10 L10 9 L13 11 L11.5 13 Q5 12.5 1 3 Z" fill="var(--sky)"/></svg>08 5550 1842</li>
    <li><svg width="14" height="14" viewBox="0 0 14 14"><rect x="1" y="3" width="12" height="8" fill="none" stroke="var(--sky)" stroke-width="1.5"/><path d="M1 3 L7 8 L13 3" fill="none" stroke="var(--sky)" stroke-width="1.5"/></svg>sam@brightharbour.tech</li>
    <li><svg width="14" height="14" viewBox="0 0 14 14"><rect x="1" y="2" width="12" height="8" fill="none" stroke="var(--sky)" stroke-width="1.5"/><rect x="4" y="11" width="6" height="1.5" fill="var(--sky)"/></svg>www.brightharbour.tech</li>
    <li style="height:auto"><svg width="14" height="14" viewBox="0 0 14 14"><path d="M1 5 L7 1 L13 5 Z M2 6 H12 V7 H2 Z M3 7 V11 H4.5 V7 Z M6.25 7 V11 H7.75 V7 Z M9.5 7 V11 H11 V7 Z M1 11.5 H13 V13 H1 Z" fill="var(--sky)"/></svg><span style="line-height:30px;margin-top:-7px">Ground floor 14 Dune st,<br>Harbourside TX 7001</span></li>
  </ul>
  <div class="abs social" aria-label="Social links"><span></span><span></span><span></span><span></span><span></span></div>
  <div class="abs rule"></div>
  <div class="abs copyright">© 2016 COMPANY NAME &nbsp;| &nbsp;ALL RIGHTS RESERVED</div>
</footer>
</body>
</html>
```